Velmor BIM business website

I have a logo design and business card concept is ongoing at this point, but i need a website design based on VDC or BIM ("Virtual Building and Construction" or "Building Information Modeling") that will stand out for the quality and concept that we provide. I am a consultant providing training and production work for Plinza (Quintavo application <where most of the overview can be obtained>). We are providing BIM production and coordination services as well. I can fill in the meat but I need an open development website. Currently, just obtaining a domain so it can be included on a business card is the quickest objective, then developing the content and launching it.

```html
<!DOCTYPE html>
<html lang="en">
<head>
<meta charset="utf-8">
<title>Velmor BIM Consulting</title>
<link rel="stylesheet" href="https://fonts.googleapis.com/css2?family=Lora:wght@400;700&family=Open+Sans:wght@400;600;700&family=Raleway:wght@600;700&display=swap">
<style>
:root{
  --navy:#1f2b5c;
  --navy-deep:#18224a;
  --hero-a:#2a3a55;
  --hero-b:#5a6478;
  --orange:#f2a53c;
  --orange-text:#e9a23b;
  --ink:#222222;
  --body:#666a73;
  --muted:#8a8d94;
  --band:#eef0f6;
  --line:#c9ccd3;
  --white:#ffffff;
}
*{box-sizing:border-box;margin:0;padding:0}
html,body{width:1200px;height:2711px;overflow:hidden}
body{position:relative;background:var(--white);font-family:"Open Sans",Arial,sans-serif;color:var(--body)}
.abs{position:absolute}
.serif{font-family:"Lora",Georgia,serif}

/* header */
.site-header{left:0;top:0;width:1200px;height:94px;background:var(--navy)}
.brand{left:99px;top:18px;display:flex;align-items:center;gap:10px}
.brand-dot{width:26px;height:26px;border-radius:50%;background:var(--orange)}
.brand-name{font-family:"Lora",Georgia,serif;font-weight:700;font-size:22px;color:var(--orange)}
.top-contact{right:100px;top:14px;display:flex;gap:22px;align-items:center;color:var(--white);font-family:"Lora",Georgia,serif;font-weight:700;font-size:17px}
.top-contact span{display:flex;align-items:center;gap:12px}
.ring{width:30px;height:30px;border-radius:50%;border:1.5px solid var(--orange);display:flex;align-items:center;justify-content:center}
.main-nav{right:100px;top:58px;display:flex;gap:32px;font-family:"Lora",Georgia,serif;font-weight:700;font-size:17px;color:var(--white)}
.main-nav .active{color:var(--orange)}

/* hero */
.hero{left:0;top:94px;width:1200px;height:436px;background:linear-gradient(90deg,var(--hero-a) 0%,#35445e 45%,var(--hero-b) 100%)}
.hero-visual{left:560px;top:94px;width:640px;height:436px;background:linear-gradient(135deg,#3b4660 0%,#6b5f7a 45%,#b88fb3 60%,#3a4258 100%);opacity:.9}
.hero-title{left:99px;top:205px;font-family:"Lora",Georgia,serif;font-weight:700;font-size:37px;color:var(--white);letter-spacing:.5px}
.hero-text{left:99px;top:268px;width:560px;font-size:16.5px;font-weight:600;line-height:28px;color:var(--white)}
.btn-ghost{left:99px;top:358px;width:181px;height:40px;border:1.5px solid var(--white);border-radius:20px;color:var(--white);font-size:14px;font-weight:700;display:flex;align-items:center;justify-content:center}
.hero-dots{left:566px;top:473px;display:flex;gap:6px}
.hero-dots i{width:12px;height:12px;border-radius:50%;border:2px solid var(--white)}
.hero-dots i.on{background:var(--white)}

/* section titles */
.section-title{left:0;width:1200px;text-align:center;font-family:"Lora",Georgia,serif;font-weight:700;font-size:25px;color:var(--ink)}
.intro{left:220px;top:640px;width:760px;text-align:center;font-size:12.5px;line-height:27px;color:var(--body)}

/* services */
.service{width:300px;text-align:center}
.service-art{margin:0 auto;width:150px;height:150px;background:radial-gradient(circle,#e6e8f1 0%,#f7f8fb 70%,var(--white) 100%)}
.service h3{margin-top:30px;font-family:"Lora",Georgia,serif;font-weight:700;font-size:21px;line-height:33px;color:var(--ink)}
.service p{margin-top:20px;font-size:12.5px;line-height:25px;color:var(--body)}
.read-more{margin-top:16px;font-size:13px;font-weight:700;color:var(--orange-text)}

/* what we do */
.band{left:0;top:1167px;width:1200px;height:414px;background:var(--band)}
.wwd-title{left:99px;top:1222px;font-family:"Lora",Georgia,serif;font-weight:700;font-size:25px;color:var(--ink)}
.wwd-text{left:99px;top:1280px;width:500px;font-size:12.5px;line-height:25px;color:var(--body)}
.wwd-text p+p{margin-top:25px}
.btn-pill{height:32px;border:1.5px solid #c6c9d2;border-radius:16px;font-size:12px;font-weight:700;color:var(--orange-text);display:flex;align-items:center;justify-content:center}
.video{left:647px;top:1229px;width:453px;height:289px;border:4px solid var(--white);box-shadow:0 1px 4px rgba(0,0,0,.15);background:linear-gradient(135deg,#0b1420 0%,#1d3a55 40%,#6f9fc0 55%,#0f1d2c 100%)}
.video-title{left:10px;top:6px;font-family:"Lora",Georgia,serif;font-weight:700;font-size:14px;color:var(--white)}
.video-play{left:201px;top:114px;width:50px;height:50px;border-radius:50%;background:rgba(0,0,0,.55);display:flex;align-items:center;justify-content:center}

/* blog */
.post-img{width:201px;height:177px;border:4px solid var(--white);box-shadow:0 0 0 1px #d5d7dd}
.post h4{font-family:"Raleway",Arial,sans-serif;font-weight:700;font-size:16px;color:var(--ink)}
.post .meta{margin-top:12px;font-size:11.5px;color:var(--body);display:flex;gap:8px;align-items:center}
.post p{margin-top:14px;width:250px;font-size:12.5px;line-height:23px;color:var(--body)}
.post .btn-pill{margin-top:14px;width:127px}

/* testimonial */
.quote-band{left:0;top:1962px;width:1200px;height:210px;background:var(--orange)}
.avatar{left:110px;top:2002px;width:126px;height:126px;border-radius:50%;border:4px solid var(--white);background:linear-gradient(160deg,#c9d3da 0%,#8fa0ad 100%)}
.quote-rule{left:270px;top:2001px;width:1.5px;height:130px;background:rgba(255,255,255,.7)}
.quote-text{left:304px;top:2005px;width:790px;font-family:"Lora",Georgia,serif;font-style:italic;font-size:14px;line-height:27px;color:var(--white)}
.quote-name{left:304px;top:2103px;font-family:"Lora",Georgia,serif;font-weight:700;font-size:18px;color:var(--white)}

/* contact */
.col-title{font-size:19px;font-weight:600;color:var(--ink)}
.field{border:1px solid #c7c9cf;font-size:11px;color:var(--muted);padding:10px 14px}
.submit{left:631px;top:2561px;width:97px;height:34px;border-radius:17px;background:var(--orange);color:var(--white);font-size:13px;font-weight:700;display:flex;align-items:center;justify-content:center}
.info-row{left:797px;display:flex;align-items:center;gap:28px;font-size:12px;line-height:24px;color:var(--body)}
.info-icon{width:34px;height:34px;border-radius:50%;border:1px solid #d0d3da;display:flex;align-items:center;justify-content:center;flex:none}
.socials{left:797px;top:2563px;display:flex;gap:10px}
.socials i{width:34px;height:34px;border-radius:50%}
.footer-rule{left:99px;top:2630px;width:1002px;height:1px;background:#cfd2d8}
.copyright{left:0;top:2663px;width:1200px;text-align:center;font-size:11.5px;color:var(--body)}
.to-top{left:1070px;top:2663px}
</style>
</head>
<body>

<header class="abs site-header">
  <div class="abs brand"><span class="brand-dot"></span><span class="brand-name">Velmor</span></div>
  <div class="abs top-contact">
    <span><span class="ring"><svg width="14" height="14" viewBox="0 0 24 24"><path fill="#f2a53c" d="M6.6 10.8a15 15 0 0 0 6.6 6.6l2.2-2.2c.3-.3.7-.4 1-.2 1.1.4 2.3.6 3.6.6.6 0 1 .4 1 1V20c0 .6-.4 1-1 1A17 17 0 0 1 3 4c0-.6.4-1 1-1h3.5c.6 0 1 .4 1 1 0 1.3.2 2.5.6 3.6.1.3 0 .7-.2 1z"/></svg></span>1 555 014 2290</span>
    <span><span class="ring"><svg width="14" height="12" viewBox="0 0 24 18"><path fill="#f2a53c" d="M0 2 12 10 24 2V0H0zM0 4v14h24V4L12 12z"/></svg></span>info@velmorbimconsulting.com</span>
  </div>
  <nav class="abs main-nav">
    <span class="active">Home</span><span>About us</span><span>Services</span><span>Blog</span><span>Resources</span><span>Contact us</span>
    <svg width="16" height="16" viewBox="0 0 24 24"><circle cx="10" cy="10" r="7" fill="none" stroke="#fff" stroke-width="3"/><path d="M15 15l7 7" stroke="#fff" stroke-width="3"/></svg>
  </nav>
</header>

<section>
  <div class="abs hero"></div>
  <div class="abs hero-visual" role="img" aria-label="Business person touching a holographic city model rising from a tablet"></div>
  <h1 class="abs hero-title">VELMOR BIM CONSULTING</h1>
  <p class="abs hero-text">Nam libero tempore, cum soluta nobis est eligendi optio cumque nihil impedit quo minus id quod maxime placeat facere.</p>
  <div class="abs btn-ghost">GET MORE INFO &gt;&gt;</div>
  <div class="abs hero-dots"><i class="on"></i><i></i><i></i><i></i></div>
</section>

<section>
  <h2 class="abs section-title" style="top:590px">WELCOME TO VELMOR BIM CONSULTING</h2>
  <p class="abs intro">Nam libero tempore, cum soluta nobis est eligendi optio cumque nihil impedit quo minus id quod maxime placeat facere pos simu nis voluptas assumenda est, omnis dolor reem quibusdam et aut officiis debitis aut rerum necessitati</p>

  <div class="abs service" style="left:121px;top:745px">
    <div class="service-art" role="img" aria-label="Line illustration of an isometric office tower"></div>
    <h3>Building<br>Information Modelling</h3>
    <p>Temporibus autem quibusdam et aut officiis debitis aut rerum necessitatibus saepe eveniet ut et voluptates repudiandae sint et</p>
    <div class="read-more">READ MORE &gt;&gt;</div>
  </div>
  <div class="abs service" style="left:450px;top:745px">
    <div class="service-art" role="img" aria-label="Line illustration of stacked isometric layers"></div>
    <h3>Training and Production<br>work for Plinza</h3>
    <p>Temporibus autem quibusdam et aut officiis debitis aut rerum necessitatibus saepe eveniet ut et voluptates repudiandae sint et</p>
    <div class="read-more">READ MORE &gt;&gt;</div>
  </div>
  <div class="abs service" style="left:808px;top:745px">
    <div class="service-art" role="img" aria-label="Line illustration of isometric building blocks of varied heights"></div>
    <h3>BIM production and<br>coordination</h3>
    <p>Temporibus autem quibusdam et aut officiis debitis aut rerum necessitatibus saepe eveniet ut et voluptates repudiandae sint et</p>
    <div class="read-more">READ MORE &gt;&gt;</div>
  </div>
</section>

<section>
  <div class="abs band"></div>
  <h2 class="abs wwd-title">WHAT WE DO</h2>
  <div class="abs wwd-text">
    <p>At vero eos et accusamus et iusto odio dignissimos ducimus qui blanditiis praesentium voluptatum deleniti atque corrupti quos dolor.</p>
    <p>Suas molestias excepturi sint occaecati cupiditate non provident, similique sunt in culpa qui officia deserunt mollitia animi, id est laborum et dolorum fuga. Et harum quidemrer um facilis est et expedita distinctio. Nam libero tempore, cum soluta nobis est eligendi optio cumque nihil impedit quo minus id quod maxime.</p>
  </div>
  <div class="abs btn-pill" style="left:99px;top:1484px;width:129px">READ MORE &gt;&gt;</div>
  <div class="abs video" role="img" aria-label="Video still of translucent blue 3D pipework model">
    <div class="abs video-title">BIM production and coordination</div>
    <div class="abs video-play"><svg width="18" height="20" viewBox="0 0 18 20"><path d="M2 1l15 9-15 9z" fill="#fff"/></svg></div>
  </div>
</section>

<section>
  <h2 class="abs section-title" style="top:1640px">OUR BLOG</h2>
  <div class="abs post-img" style="left:99px;top:1720px;background:linear-gradient(135deg,#d9d2c6 0%,#b9aa98 50%,#eeeae4 100%)" role="img" aria-label="Smiling woman in glasses working at a laptop"></div>
  <div class="abs post" style="left:329px;top:1716px">
    <h4>FINIBUS BONORUM ET MALORU</h4>
    <div class="meta"><span>&#9634; 08/03/2016</span><span>|</span><span>&#9679; Alan Brooks</span></div>
    <p>Nam libero tempore, cum soluta nobises tei lig endi optio cumque nihil impedit qu minus id quod maxime plac.</p>
    <div class="btn-pill">READ MORE &gt;&gt;</div>
  </div>
  <div class="abs post-img" style="left:625px;top:1720px;background:linear-gradient(135deg,#0a1e45 0%,#2a6fb0 50%,#0b2550 100%)" role="img" aria-label="Digital globe with blue data grid"></div>
  <div class="abs post" style="left:858px;top:1716px">
    <h4>FINIBUS BONORUM ET MALORU</h4>
    <div class="meta"><span>&#9634; 08/03/2016</span><span>|</span><span>&#9679; Alan Brooks</span></div>
    <p>Nam libero tempore, cum soluta nobises tei lig endi optio cumque nihil impedit qu minus id quod maxime plac.</p>
    <div class="btn-pill">READ MORE &gt;&gt;</div>
  </div>
</section>

<section>
  <div class="abs quote-band"></div>
  <svg class="abs" style="left:36px;top:2052px" width="18" height="30" viewBox="0 0 18 30"><path d="M15 2 3 15l12 13" fill="none" stroke="#fff" stroke-width="2.5"/></svg>
  <svg class="abs" style="left:1146px;top:2052px" width="18" height="30" viewBox="0 0 18 30"><path d="M3 2l12 13L3 28" fill="none" stroke="#fff" stroke-width="2.5"/></svg>
  <div class="abs avatar" role="img" aria-label="Portrait of the client giving the testimonial"></div>
  <div class="abs quote-rule"></div>
  <p class="abs quote-text">Nam libero tempore, cum soluta nobis est eligendi optio cumque nihil impedit quo minus id quod maxime placeat facere possimus, omnis voluptas assumenda est, omnis dolor repellendus. Temporibus autem quibusdam et aut officiis debitis aut rerum necessitatibus saepe eveniet ut et voluptates repudiandae sint et molestiae</p>
  <div class="abs quote-name">– Marcel Dufresne</div>
</section>

<section>
  <h2 class="abs section-title" style="top:2238px">CONTACT US</h2>
  <div class="abs col-title" style="left:99px;top:2304px">Get in touch</div>
  <div class="abs field" style="left:99px;top:2371px;width:311px;height:32px">Name :</div>
  <div class="abs field" style="left:417px;top:2371px;width:311px;height:32px">Phone no :</div>
  <div class="abs field" style="left:99px;top:2416px;width:629px;height:32px">Email :</div>
  <div class="abs field" style="left:99px;top:2461px;width:629px;height:81px">Message :</div>
  <div class="abs submit">SUBMIT</div>

  <div class="abs col-title" style="left:797px;top:2304px">Contact Information</div>
  <div class="abs info-row" style="top:2356px">
    <span class="info-icon"><svg width="12" height="16" viewBox="0 0 12 16"><path d="M6 0a6 6 0 0 0-6 6c0 4.5 6 10 6 10s6-5.5 6-10a6 6 0 0 0-6-6zm0 8.5A2.5 2.5 0 1 1 6 3.5a2.5 2.5 0 0 1 0 5z" fill="#1f2b5c"/></svg></span>
    <span>2740 Larkspur Way #310,<br>Cedar Point, FL 33918</span>
  </div>
  <div class="abs info-row" style="top:2415px">
    <span class="info-icon"><svg width="13" height="13" viewBox="0 0 24 24"><path fill="#1f2b5c" d="M6.6 10.8a15 15 0 0 0 6.6 6.6l2.2-2.2c.3-.3.7-.4 1-.2 1.1.4 2.3.6 3.6.6.6 0 1 .4 1 1V20c0 .6-.4 1-1 1A17 17 0 0 1 3 4c0-.6.4-1 1-1h3.5c.6 0 1 .4 1 1 0 1.3.2 2.5.6 3.6.1.3 0 .7-.2 1z"/></svg></span>
    <span>1 555 014 2290</span>
  </div>
  <div class="abs info-row" style="top:2458px">
    <span class="info-icon"><svg width="13" height="13" viewBox="0 0 14 14"><rect x="1" y="4" width="12" height="9" rx="1" fill="#1f2b5c"/><rect x="3" y="1" width="8" height="4" fill="#1f2b5c"/><rect x="4" y="7" width="6" height="3" fill="#fff"/></svg></span>
    <span>1 555 014 7731</span>
  </div>
  <div class="abs info-row" style="top:2507px">
    <span class="info-icon"><svg width="13" height="10" viewBox="0 0 24 18"><path fill="#1f2b5c" d="M0 2 12 10 24 2V0H0zM0 4v14h24V4L12 12z"/></svg></span>
    <span>info@velmorbimconsulting.com</span>
  </div>
  <div class="abs socials"><i style="background:#3b5998"></i><i style="background:#2aa3ef"></i><i style="background:#a1755c"></i><i style="background:#cb2027"></i></div>

  <div class="abs footer-rule"></div>
  <p class="abs copyright">Copyrights © 2017, Velmor Bim Consulting. All Rights Reserved.</p>
  <svg class="abs to-top" width="28" height="16" viewBox="0 0 28 16"><path d="M2 14 14 3l12 11" fill="none" stroke="#8a8d94" stroke-width="2.5"/></svg>
</section>

</body>
</html>
```